Fahrzeugbeschriftung für Zimmerei
Zielgruppe
Zimmerei
Aufgabenstellung
Die Beschriftung soll auf einen kurzen Norka Velmo Baujahr 2018 mit Hochdach und der Farbe weiß. Hecktüren und Seitentür sind ohne Fenster. Insgesamt sollte das Erscheinungsbild nicht zu aufdringlich, eher schlicht gestaltet werden.
Logo habe ich als PDF hochgeladen. Zusätzlich soll die Telefonnummer auf den Bus. Tätigkeiten wie Holzbau, Holzterrassen, Holzbalkone, Haustürüberdachungen, Carports und Dacharbeiten sollten auch drauf.

```html
<!DOCTYPE html>
<html lang="de">
<head>
<meta charset="utf-8">
<title>Fahrzeugbeschriftung Zimmerei Brandtner</title>
<link rel="stylesheet" href="https://fonts.googleapis.com/css2?family=Montserrat:ital,wght@0,500;0,600;0,700;1,800&display=swap">
<style>
  :root {
    --teal: #1f6b7f;
    --teal-dark: #185a6b;
    --stripe-grey: #8e8f91;
    --rule-grey: #d9dadb;
    --body-dark: #4a4b4d;
    --white: #ffffff;
    --paper: #f5f6f7;
  }
  html, body {
    margin: 0;
    width: 1200px;
    height: 900px;
    overflow: hidden;
    background: var(--paper);
    font-family: "Montserrat", sans-serif;
  }
  .wrap-layout {
    position: absolute;
    left: 40px;
    top: 120px;
    width: 1120px;
    height: 660px;
    background: var(--white);
    overflow: hidden;
  }
  .brand {
    position: absolute;
    left: 330px;
    top: 70px;
    display: flex;
    align-items: center;
    gap: 36px;
  }
  .brand-square {
    width: 150px;
    height: 150px;
    background: var(--teal);
  }
  .brand-name {
    color: var(--teal);
    font-weight: 600;
    line-height: 1.05;
    letter-spacing: 2px;
  }
  .brand-name span { display: block; }
  .brand-line-1 { font-size: 56px; }
  .brand-line-2 { font-size: 64px; }
  .web-band {
    position: absolute;
    left: 440px;
    top: 300px;
    width: 680px;
    height: 48px;
    background: var(--stripe-grey);
  }
  .web-rule {
    position: absolute;
    left: 0;
    top: 348px;
    width: 100%;
    height: 2px;
    background: var(--rule-grey);
  }
  .web-address {
    position: absolute;
    right: 40px;
    top: 306px;
    color: var(--white);
    font-weight: 700;
    font-size: 22px;
    letter-spacing: 0.5px;
  }
  .service-band {
    position: absolute;
    left: 0;
    top: 358px;
    width: 100%;
    height: 140px;
    background: var(--teal);
  }
  .phone {
    position: absolute;
    left: 70px;
    top: 30px;
    color: var(--white);
    font-weight: 800;
    font-style: italic;
    font-size: 34px;
    letter-spacing: 0.5px;
  }
  .services {
    position: absolute;
    left: 440px;
    top: 16px;
    margin: 0;
    color: var(--white);
    font-weight: 500;
    font-size: 17px;
    line-height: 1.3;
    text-align: center;
    letter-spacing: 0.5px;
  }
  .lower-band {
    position: absolute;
    left: 0;
    top: 498px;
    width: 100%;
    height: 110px;
    background: var(--body-dark);
  }
  .sill-band {
    position: absolute;
    left: 0;
    top: 608px;
    width: 100%;
    height: 40px;
    background: var(--teal-dark);
  }
</style>
</head>
<body>
  <main class="wrap-layout">
    <div class="brand">
      <div class="brand-square"></div>
      <div class="brand-name">
        <span class="brand-line-1">ZIMMEREI</span>
        <span class="brand-line-2">BRANDTNER</span>
      </div>
    </div>

    <div class="web-band"></div>
    <div class="web-rule"></div>
    <div class="web-address">www.zimmerei-brandtner.example</div>

    <section class="service-band">
      <div class="phone">0123 456 789</div>
      <p class="services">
        Holzbau | Holzterrassen<br>
        Holzbalkone | Haustürüberdachungen<br>
        Carports | Dacharbeiten können
      </p>
    </section>
    <div class="lower-band"></div>
    <div class="sill-band"></div>
  </main>
</body>
</html>
```